Small soho-London based IT Support company website

We've had our logo and stationary redesigned on Sketch Harbor and now we'd like our website done.
We're a small IT support company. Our client base is mainly design studios and advertising agencies working mainly on Macs.
As such our website needs to be young clean and professional looking.
Our current site can be viewed at http://brisk-node.example
We currently use Joomla but we're happy to move to Wordpress if that's the only option.
Industry/Entity Type
Advertising
Look and feel
Each slider illustrates characteristics of the customer's brand and the style your logo design should communicate.

```html
<!DOCTYPE html>
<html lang="en">
<head>
<meta charset="utf-8">
<title>Brisk Node – Services</title>
<link rel="stylesheet" href="https://fonts.googleapis.com/css2?family=Quicksand:wght@300;400;500&family=Ubuntu:wght@400;500&family=Arimo:wght@400;700&display=swap">
<style>
:root{
  --night:#1c2026;
  --night-deep:#14171c;
  --bar:#2c3139;
  --bar-edge:#3a404a;
  --lime:#c6d82b;
  --paper:#ffffff;
  --mist:#ececec;
  --ink:#1d1f22;
  --copy:#8f9296;
  --side-text:#555a60;
  --rule:#e2e2e2;
  --foot-text:#5e6670;
  --foot-head:#8a9bb2;
  --sky:#6fb7e6;
  --nav:#c9ccd0;
  --promo-hot:#ee5a1c;
  --promo-deep:#b8160f;
}
*{margin:0;padding:0;box-sizing:border-box}
html,body{width:1107px;height:1200px;overflow:hidden;background:var(--mist)}
.page{position:relative;width:1000px;height:1084px;transform:scale(1.107);transform-origin:0 0;font-family:"Arimo",Arial,sans-serif}
.top-band{position:absolute;left:0;top:0;width:1000px;height:342px;background:radial-gradient(ellipse at 50% 30%,#2a2f37 0%,var(--night) 55%,var(--night-deep) 100%)}
.mist-band{position:absolute;left:0;top:342px;width:1000px;height:582px;background:var(--mist)}
.brand{position:absolute;left:146px;top:16px;font-family:"Quicksand",sans-serif;font-weight:500;font-size:40px;color:var(--lime);letter-spacing:-.5px}
.contact-strip{position:absolute;right:132px;top:11px;display:flex;gap:22px;font-size:10px;color:var(--lime);align-items:center}
.contact-strip span{display:flex;align-items:center;gap:6px}
.main-nav{position:absolute;left:135px;top:47px;width:733px;height:39px;border-bottom:1px solid #3a3f47}
.main-nav a{position:absolute;top:5px;font-size:10px;color:var(--nav);text-decoration:none;letter-spacing:.2px}
.main-nav a.current::after{content:"";position:absolute;left:-11px;right:-11px;top:30px;height:3px;background:#c8c8c8}
.welcome{position:absolute;left:0;width:1000px;top:112px;text-align:center;font-family:"Quicksand",sans-serif;font-weight:300;font-size:34px;color:#f2f2f2;letter-spacing:.3px}
.welcome em{font-style:normal;color:var(--lime)}
.section-bar{position:absolute;left:135px;top:185px;width:733px;height:60px;background:linear-gradient(#333841,var(--bar));border-top:1px solid var(--bar-edge)}
.section-bar h1{position:absolute;left:15px;top:13px;font-family:"Quicksand",sans-serif;font-weight:400;font-size:27px;color:var(--lime)}
.gear{position:absolute;right:8px;top:2px;width:84px;height:56px;background:radial-gradient(ellipse at 55% 50%,#cfcfcf 0%,#8a8a8a 50%,rgba(44,49,57,0) 75%)}
.panel{position:absolute;left:135px;top:245px;width:733px;height:679px;background:var(--paper)}
.side{position:absolute;left:15px;top:0;width:197px;height:400px;border-right:1px solid #eee}
.side h2,.partners h2{font-family:"Ubuntu",sans-serif;font-weight:400;font-size:13px;color:var(--ink)}
.side h2{position:absolute;top:12px}
.service-list{position:absolute;top:40px;left:5px;width:150px;list-style:none}
.service-list li{height:27px;border-bottom:1px solid var(--rule);font-family:"Ubuntu",sans-serif;font-size:9.5px;color:var(--side-text);padding:7px 0 0 13px;position:relative}
.service-list li::before{content:"";position:absolute;left:2px;top:9px;border:4px solid transparent;border-left:5px solid #aaa;border-right:0}
.partners{position:absolute;left:15px;top:412px;width:197px}
.partner-name{margin:14px 0 0 42px;font-family:"Arimo",sans-serif;font-weight:700;font-size:15px;color:#333;display:flex;align-items:center;gap:6px}
.partner-name i{width:10px;height:10px;border-radius:50%;background:#d0202a;display:inline-block}
.promo{margin-top:7px;width:197px;height:183px;background:radial-gradient(circle at 50% 50%,var(--promo-hot) 0%,var(--promo-deep) 100%)}
.hero{position:absolute;left:226px;top:15px;width:492px;height:161px;background:linear-gradient(100deg,#3a3d42 0%,#8e9196 45%,#5a5d62 70%,#1f2124 100%)}
.intro{position:absolute;left:227px;top:189px;width:492px;font-size:11.5px;line-height:16.5px;color:var(--copy)}
.intro p{margin-bottom:16.5px}
.footer{position:absolute;left:0;top:924px;width:1000px;height:160px;background:linear-gradient(#23272e,var(--night-deep))}
.foot-head{position:absolute;left:135px;top:13px;width:395px;font-size:8.5px;color:var(--foot-head);border-bottom:1px solid #3a3f47;padding-bottom:5px}
.foot-col{position:absolute;list-style:none;font-family:"Ubuntu",sans-serif;font-size:9.5px;color:var(--foot-text);line-height:16.5px}
.subscribe{position:absolute;left:653px;top:12px;width:215px;height:94px;background:#1a1d22;border-radius:4px;padding:8px 12px}
.subscribe .big{font-family:"Quicksand",sans-serif;font-size:22px;color:#e8e8e8;line-height:22px;letter-spacing:1px}
.subscribe .small{font-family:"Quicksand",sans-serif;font-size:14px;color:var(--sky);line-height:15px;letter-spacing:.5px}
.signup{position:absolute;left:13px;top:56px;width:188px;height:30px;background:#0c0e11;border:1px solid #2a2e35;border-radius:3px}
.signup span{position:absolute;right:0;top:0;height:28px;width:64px;background:#23272e;color:var(--lime);font-family:"Quicksand",sans-serif;font-size:15px;text-align:center;line-height:28px}
.foot-base{position:absolute;left:135px;top:128px;width:733px;border-top:1px solid #30353d;padding-top:10px;font-size:8.5px;color:var(--foot-text);display:flex;justify-content:space-between}
.social{display:flex;gap:4px;align-items:center}
.social i{width:11px;height:11px;display:inline-block;border-radius:2px}
</style>
</head>
<body>
<div class="page">
  <div class="top-band"></div>
  <div class="mist-band"></div>

  <div class="brand">Brisk Node</div>
  <div class="contact-strip">
    <span><svg width="11" height="11" viewBox="0 0 12 12"><path d="M2 1l2 0 1 3-1.5 1a7 7 0 0 0 3.5 3.5L8 7l3 1v2a1 1 0 0 1-1 1A9 9 0 0 1 1 2a1 1 0 0 1 1-1z" fill="#9aa0a8"/></svg>PHONE : 0203 555 0142</span>
    <span><svg width="12" height="9" viewBox="0 0 12 9"><rect width="12" height="9" fill="#9aa0a8"/><path d="M0 0l6 5 6-5" stroke="#1c2026" fill="none"/></svg>EMAIL US</span>
  </div>
  <nav class="main-nav">
    <a style="left:362px">HOME</a>
    <a style="left:429px">ABOUT US</a>
    <a class="current" style="left:514px">SERVICES</a>
    <a style="left:602px">WHY US</a>
    <a style="left:678px">CONTACT</a>
  </nav>

  <div class="welcome">Welcome to <em>Brisk</em> Technical Services</div>

  <div class="section-bar">
    <h1>Services</h1>
    <div class="gear" role="img" aria-label="Silver gear icon"></div>
  </div>

  <div class="panel">
    <aside class="side">
      <h2>Our Services</h2>
      <ul class="service-list">
        <li>Regular Maintenance</li><li>Monitoring</li><li>Remote Support</li><li>Emergency Support</li>
        <li>IT Manager</li><li>IT Roadmap</li><li>Asset Management</li><li>Online Backup</li>
        <li>Tape pickup</li><li>Email Spam &amp; Virus filtering</li><li>Network Virus protection</li><li>Night Work</li>
      </ul>
    </aside>
    <div class="partners">
      <h2>Partners</h2>
      <div class="partner-name"><i></i>VAULTLINE</div>
      <div class="promo" role="img" aria-label="Partner advert banner for an online backup service"></div>
    </div>

    <div class="hero" role="img" aria-label="Photo of a hand touching a red screen panel"></div>
    <div class="intro">
      <p>We provide many services here at Brisk. We aim to be your complete outsourced IT department, supplying you with everything from hardware / software and technical support, to detailed IT road maps and capital expenditure plans.</p>
      <p>We can proactively manage your entire infrastructure, or assist your existing technical staff. Whatever your requirements are, we will tailor a support package to fit your needs.</p>
      <p>Have a browse through our services, and feel free to call us if you'd like to discuss anything..</p>
    </div>
  </div>

  <footer class="footer">
    <div class="foot-head">OUR SERVICES</div>
    <ul class="foot-col" style="left:135px;top:33px"><li>Regular Maintenance</li><li>Monitoring</li><li>Remote Support</li><li>Emergency Support</li></ul>
    <ul class="foot-col" style="left:278px;top:38px"><li>IT Manager</li><li>IT Roadmap</li><li>Asset Management</li><li>Online Backup</li></ul>
    <ul class="foot-col" style="left:403px;top:38px"><li>Tape pickup</li><li>Email Spam &amp; Virus filtering</li><li>Network Virus protection</li><li>Night Work</li></ul>
    <div class="subscribe">
      <div class="big">SUBSCRIBE</div>
      <div class="small">TO OUR NEWSLETTER</div>
      <div class="signup"><span>Sign Up</span></div>
    </div>
    <div class="foot-base">
      <div class="social">FOLLOW US ON:&nbsp;<i style="background:#4a66a0"></i><i style="background:#3aa3d8"></i><i style="background:#2f78b0"></i></div>
      <div>© BRISK NODE LTD 2011</div>
    </div>
  </footer>
</div>
</body>
</html>
```